Business Card for innovative, tech/consultant company

We are specializing in bringing together Efficiency methodology and Technology for our Business customers. We would like an astonishing business Card that matches this idea.

Target Market(s)

Businesses of medium size or more

Industry/Entity Type

Business Consultant

Contact Information for Business Card

Name, Title, personal email, www, address, phone

Font styles to use
Sans Serif

Colors
3277b5

Requirements
Must have
• - innovative, efficient design
• - good readable
• - Colors must match our logo (blue and grey)
• - the attached font (is licensed by our Company) must be used (Syntax LT)
Should not have
• overloaded

```html
<!DOCTYPE html>
<html lang="en">
<head>
<meta charset="UTF-8">
<title>Vantrel Business Card</title>
<link href="https://fonts.googleapis.com/css2?family=Source+Sans+3:wght@400;500&display=swap" rel="stylesheet">
<style>
  :root {
    --brand-blue: #0a7fc4;
    --brand-grey: #7a7a7c;
    --ink: #2a2a2a;
    --paper: #ffffff;
    --backdrop: #1c1c1c;
  }
  * { margin: 0; padding: 0; box-sizing: border-box; }
  html, body {
    width: 1200px;
    height: 900px;
    overflow: hidden;
    background: var(--backdrop);
    font-family: "Source Sans 3", "Helvetica Neue", Arial, sans-serif;
  }
  .stage { position: relative; width: 1200px; height: 900px; }

  .card {
    position: absolute;
    top: 170px;
    width: 347px;
    height: 561px;
    overflow: hidden;
  }
  .card--front { left: 259px; background: var(--paper); }
  .card--back { left: 631px; background: var(--brand-blue); }

  .tab {
    position: absolute;
    left: 102px;
    width: 143px;
    height: 30px;
    background: var(--brand-blue);
  }
  .tab--top { top: 0; }
  .tab--bottom { bottom: 0; }

  .wordmark {
    position: absolute;
    font-weight: 400;
    letter-spacing: -1px;
    line-height: 1;
    white-space: nowrap;
  }
  .card--front .wordmark {
    top: 128px;
    left: 0;
    width: 100%;
    text-align: center;
    font-size: 88px;
    color: var(--brand-grey);
  }
  .card--back .wordmark {
    top: 406px;
    left: 40px;
    font-size: 92px;
    color: var(--paper);
  }

  .contact {
    position: absolute;
    left: 0;
    width: 100%;
    text-align: center;
    color: var(--ink);
  }
  .person { top: 276px; }
  .person__name {
    font-size: 26px;
    font-weight: 400;
    color: var(--brand-blue);
    line-height: 1.1;
  }
  .person__title { font-size: 16px; margin-top: 4px; }

  .channels { top: 347px; font-size: 16px; line-height: 21px; }
  .channel { display: flex; justify-content: center; align-items: center; gap: 9px; }
  .channel svg { width: 11px; height: 11px; flex: none; }

  .address { top: 465px; font-size: 16px; line-height: 17px; }
</style>
</head>
<body>
  <main class="stage">
    <section class="card card--front">
      <div class="tab tab--top"></div>

      <div class="wordmark">Vantrel</div>

      <div class="contact person">
        <p class="person__name">JOHN SMITH</p>
        <p class="person__title">Managing Director</p>
      </div>

      <div class="contact channels">
        <p class="channel">
          <svg viewBox="0 0 12 12" aria-hidden="true"><path fill="#0a7fc4" d="M1 4c0-2 2-3 5-3s5 1 5 3l-2 1-1-1.5H4L3 5zM3 6h6l1 4H2z"/></svg>
          823-456-7890
        </p>
        <p class="channel">
          <svg viewBox="0 0 12 12" aria-hidden="true"><rect x="1" y="3" width="10" height="7" fill="#0a7fc4"/><path d="M1.5 3.5L6 7l4.5-3.5" fill="none" stroke="#fff" stroke-width="0.9"/></svg>
          info@youremail.com
        </p>
      </div>

      <div class="contact address">
        <p>1234, Address Goes Here</p>
        <p>Country Name, 123456</p>
      </div>

      <div class="tab tab--bottom"></div>
    </section>

    <section class="card card--back">
      <div class="wordmark">Vantrel</div>
    </section>
  </main>
</body>
</html>
```